Business Card Design

Im electrician in melbourne after a business cards. I have no logos done. I have attached a card that i like but needs to be altered to my business name, so in the picture shows a lead plug into a socket spelling plug, i want the spelling replaced with my company name. I was thinking some thing with a charcoal back ground with yellow or green font.
I have wrote what I'd like above but feel free to try your own ideas and designs.
Industry/Entity Type
Electrician
Contact Information for Business Card
Vorn Electrical Services PTY LTD (Display on the front of card, the PTY LTD can be in small font)
REC:58104 (also on the front in small font)
Call Teodor (back i dont want my last name on the card)
Phone: 0488157093 (back
Email: vornelectricalservices@kestramail.com (back)
Domestic, Commercial, Industrial, (on the back in dot points.)
Look and feel
Each slider illustrates characteristics of the customer's brand and the style your logo design should communicate.

```html
<!DOCTYPE html>
<html lang="en">
<head>
<meta charset="utf-8">
<title>Vorn Electrical Services – Business Card</title>
<link href="https://fonts.googleapis.com/css2?family=Arimo&family=Montserrat:wght@600;700&family=Questrial&display=swap" rel="stylesheet">
<style>
  :root {
    --charcoal-dark: #353333;
    --charcoal-mid: #4e4c4b;
    --charcoal-light: #7c7b7a;
    --volt-yellow: #ffff2e;
    --band-yellow: #fff200;
    --band-olive: #4f4d2c;
    --band-silver: #ffffff;
    --band-steel: #434242;
    --text-white: #ffffff;
    --rule-grey: #bdbdbd;
  }
  html, body {
    margin: 0;
    padding: 0;
    width: 1200px;
    height: 725px;
    overflow: hidden;
    background: var(--charcoal-dark);
  }
  p, h1, ul { margin: 0; padding: 0; }
  .card {
    position: relative;
    width: 1200px;
    height: 725px;
    overflow: hidden;
    background: radial-gradient(ellipse 640px 520px at 600px 330px,
      var(--charcoal-light) 0%, var(--charcoal-mid) 55%, var(--charcoal-dark) 100%);
    color: var(--text-white);
  }
  .brand {
    position: absolute;
    right: 24px;
    top: 16px;
    width: 580px;
    text-align: center;
    color: var(--volt-yellow);
    font-family: "Montserrat", sans-serif;
    font-weight: 600;
    white-space: nowrap;
  }
  .brand-name {
    font-weight: 600;
    line-height: 1;
    letter-spacing: -1px;
  }
  .brand-name .line-one { display: block; font-size: 60px; }
  .brand-name .line-two { display: block; font-size: 60px; margin-top: 6px; }
  .brand-legal {
    margin-top: 10px;
    font-size: 20px;
    line-height: 1;
    letter-spacing: 1px;
  }
  .contact-name {
    position: absolute;
    left: 97px;
    top: 212px;
    font-family: "Montserrat", sans-serif;
    font-weight: 700;
    font-size: 54px;
    line-height: 1;
  }
  .divider {
    position: absolute;
    left: 0;
    top: 299px;
    width: 870px;
    height: 3px;
    background: linear-gradient(90deg, var(--rule-grey) 0%, var(--rule-grey) 55%, rgba(189,189,189,0) 100%);
  }
  .contact-row {
    position: absolute;
    left: 96px;
    display: flex;
    align-items: center;
    font-family: "Questrial", sans-serif;
    line-height: 1;
    white-space: nowrap;
  }
  .contact-row svg { flex: none; }
  .contact-row.phone { top: 342px; font-size: 50px; }
  .contact-row.email { top: 424px; font-size: 38px; }
  .contact-row .value { margin-left: 52px; }
  .contact-row.email .value { margin-left: 52px; }
  .band {
    position: absolute;
    left: 0;
    width: 1200px;
  }
  .band.yellow {
    height: 52px;
    background: linear-gradient(90deg, var(--band-olive) 0%, #c9c41a 25%, var(--band-yellow) 50%, #c9c41a 75%, var(--band-olive) 100%);
  }
  .band.silver {
    top: 549px;
    height: 52px;
    background: linear-gradient(90deg, var(--band-steel) 0%, #a9a9a9 28%, var(--band-silver) 50%, #a9a9a9 72%, var(--band-steel) 100%);
  }
  .band.top { top: 479px; }
  .band.bottom { top: 618px; }
  .services {
    position: absolute;
    left: 38px;
    right: 36px;
    top: 678px;
    list-style: none;
    display: flex;
    justify-content: space-between;
    font-family: "Arimo", sans-serif;
    font-size: 38px;
    line-height: 1;
    letter-spacing: 0.5px;
  }
</style>
</head>
<body>
  <main class="card">
    <div class="brand">
      <h1 class="brand-name">
        <span class="line-one">vorn electrical</span>
        <span class="line-two">services</span>
      </h1>
      <p class="brand-legal">PTY LTD &nbsp;·&nbsp; REC:58104</p>
    </div>

    <p class="contact-name">Call Teodor</p>
    <div class="divider"></div>

    <p class="contact-row phone">
      <svg width="58" height="46" viewBox="0 0 58 46" aria-hidden="true" fill="none" stroke="#ffffff" stroke-width="2.4" stroke-linejoin="round">
        <path d="M4 15 C4 5 54 5 54 15 L54 19 L42 19 L42 13 L16 13 L16 19 L4 19 Z"/>
        <path d="M16 19 L12 42 L46 42 L42 19 Z"/>
        <circle cx="29" cy="31" r="6.5"/>
        <circle cx="29" cy="31" r="2"/>
      </svg>
      <span class="value">0488157093</span>
    </p>

    <p class="contact-row email">
      <svg width="56" height="32" viewBox="0 0 56 32" aria-hidden="true" fill="none" stroke="#ffffff" stroke-width="2.4" stroke-linejoin="round">
        <rect x="2" y="2" width="52" height="28"/>
        <path d="M2 2 L28 20 L54 2"/>
        <path d="M2 30 L22 15 M54 30 L34 15"/>
      </svg>
      <span class="value">vornelectricalservices@kestramail.com</span>
    </p>

    <div class="band yellow top"></div>
    <div class="band silver"></div>
    <div class="band yellow bottom"></div>

    <ul class="services">
      <li>DOMESTIC</li>
      <li>COMMERCIAL</li>
      <li>INDUSTRIAL</li>
    </ul>
  </main>
</body>
</html>
```